KINDRED: Social Media Post COVID-19 & Flu #1

- Create a similar design for a Social Media Post Image
- Attached, Logo, sample flu social media image.
- KINDRED - must be included - in the colors provided (see attachment)
- Protect your community. Protect Your Elders. Stay Vaccinated. - must be include
-COVID-19 & Flu - will be stated somewhere
- image of mom and sons
-might include boarder
- inspiration at https://volmerhaven.org/, and https://www.facebook.com/Volmerhaven

```html
<!DOCTYPE html>
<html lang="en">
<head>
<meta charset="utf-8">
<title>KINDRED – COVID-19 &amp; Flu Vaccination Campaign</title>
<link rel="stylesheet" href="https://fonts.googleapis.com/css2?family=Montserrat:wght@600;700;800;900&family=Source+Serif+4:wght@700&display=swap">
<style>
  :root {
    --teal: #4ea8b2;
    --wine: #911f30;
    --blush: #e4c4c4;
    --white: #ffffff;
    --border-teal: #7fa3a6;
    --border-rose: #b77a80;
    --photo-top: #a77c76;
    --photo-bottom: #5a3f43;
  }
  * { margin: 0; padding: 0; box-sizing: border-box; }
  html, body { width: 1200px; height: 1196px; overflow: hidden; background: var(--white); }
  .post {
    position: relative;
    width: 1200px;
    height: 1196px;
    overflow: hidden;
    font-family: "Montserrat", sans-serif;
    background: linear-gradient(135deg, var(--border-teal), var(--border-rose) 50%, var(--border-teal));
  }
  .post__field {
    position: absolute;
    left: 34px; top: 32px; right: 34px; bottom: 32px;
    background: var(--blush);
    border: 9px solid var(--wine);
  }
  .title-frame {
    position: absolute;
    left: 76px; top: 73px;
    width: 823px; height: 205px;
    border: 13px solid var(--wine);
  }
  .title-frame__word {
    position: absolute;
    left: 0; right: 0; top: 20px;
    text-align: center;
    color: var(--teal);
    font-weight: 900;
    font-size: 134px;
    line-height: 1;
    letter-spacing: 4px;
  }
  .campaign-band {
    position: absolute;
    left: 135px; top: 237px;
    width: 704px; height: 60px;
    background: var(--wine);
    color: var(--white);
    font-family: "Source Serif 4", serif;
    font-weight: 700;
    font-size: 29px;
    letter-spacing: 1.6px;
    line-height: 60px;
    text-align: center;
  }
  .org-name {
    position: absolute;
    left: 935px; top: 110px;
    width: 185px;
    color: var(--teal);
    font-weight: 700;
    font-size: 18px;
    line-height: 1.25;
    text-align: center;
    text-transform: uppercase;
  }
  .org-name__mark {
    display: block;
    width: 70px; height: 70px;
    margin: 0 auto 14px;
    background: var(--teal);
  }
  .family-photo {
    position: absolute;
    left: 230px; top: 472px;
    width: 702px; height: 683px;
    background: linear-gradient(180deg, var(--photo-top), var(--photo-bottom));
    z-index: 1;
  }
  .headline {
    position: absolute;
    left: 0; right: 0;
    text-align: center;
    font-weight: 800;
    font-size: 75px;
    line-height: 1;
    -webkit-text-stroke: 7px var(--white);
    paint-order: stroke fill;
    filter: drop-shadow(3px 4px 3px rgba(90, 30, 40, 0.35));
    z-index: 3;
  }
  .headline--community { top: 332px; }
  .headline--elders { top: 420px; }
  .headline__teal { color: var(--teal); }
  .headline__wine { color: var(--wine); }
  .stay-band {
    position: absolute;
    left: 255px; top: 798px;
    width: 615px; height: 121px;
    background: rgba(235, 225, 225, 0.55);
    z-index: 2;
  }
  .stay-line {
    position: absolute;
    left: 0; right: 0; top: 812px;
    padding-right: 14px;
    text-align: center;
    color: var(--teal);
    font-weight: 800;
    font-size: 97px;
    line-height: 1;
    letter-spacing: 2px;
    -webkit-text-stroke: 7px var(--white);
    paint-order: stroke fill;
    filter: drop-shadow(3px 4px 3px rgba(60, 30, 40, 0.35));
    z-index: 3;
  }
  .learn-band {
    position: absolute;
    left: 45px; top: 1018px;
    width: 1110px; height: 88px;
    background: rgba(145, 31, 48, 0.92);
    color: var(--white);
    font-weight: 700;
    font-size: 28.5px;
    letter-spacing: 1.3px;
    line-height: 88px;
    text-align: center;
    z-index: 3;
  }
</style>
</head>
<body>
  <main class="post">
    <div class="post__field"></div>

    <div class="title-frame">
      <h1 class="title-frame__word">KINDRED</h1>
    </div>
    <p class="campaign-band">COVID-19 &amp; FLU VACCINATION CAMPAIGN</p>

    <p class="org-name"><span class="org-name__mark"></span>Volmerhaven Elder Alliance</p>

    <div class="family-photo" role="img" aria-label="Photo of a smiling mother hugged by her two sons, seated outdoors on a patterned blanket"></div>

    <h2 class="headline headline--community"><span class="headline__teal">Protect Your</span> <span class="headline__wine">Community</span></h2>
    <h2 class="headline headline--elders"><span class="headline__teal">Protect Your</span> <span class="headline__wine">Elders</span></h2>

    <div class="stay-band"></div>
    <p class="stay-line">Stay Vaccinated</p>

    <p class="learn-band">Learn more about getting vaccinated against COVID-19 &amp; the Flu</p>
  </main>
</body>
</html>
```